Gentle Willow Pregnancy and Baby Massage

I need a web design for a new business, GENTLE WILLOW PREGNANCY AND BABY MASSAGE that I am in the process of setting up in the suburbs of Perth, Western Australia. The business is owned and operated by myself and my intention is to service Pregnant Mothers and Parents of Young Babies that would benefit from massage. I would like to have a "Home Page" and pages for "About Me", "Pregnancy Massage", "Baby Massage", a Pricing Page for Pregnancy Massage Sessions, a Pricing Page for Baby Massage Sessions, and a "Contact Me" page to allow clients to either contact me with queries or book available pregnancy massage sessions on a particular day of the week. I would also like a "News" page that would include articles I have written, news about new courses and a link to my Chatterlane page (yet to be set up). I would like to keep the colour schemes similar to my logo design colours. I need the design to be easy to follow and to appeal to a younger audience (20's to mid 30's).
The target audience is pregnant mothers-to-be wishing to receive massage treatments, and new parents and grandparents of small babies that would like to learn how to massage their babies.
The look and feel should be modern, professional, elegant and feminine.
I need the design to be in a standard format such that I can update the content by myself ( and does not need specialised software) as the company and business progresses.

Target Market(s)

Industry/Entity Type

Health And Wellness

Contact Information for Business Card

Card should have rounded edges. Design should have the same "feel" as the website. Contact Details of my business address, mobile phone, email and website should be included.

Coding

Coded - Design and coding required

Number of Pages Required

5+ page

Font styles to use
Script

Requirements
Must have
• Same colours as logo design. In cmyk system, the colours are: 20,60,0,0 which best result is tintora 681 and 40,40,0,0 which best result is tintora 2645. Card should include the logo design.

```html
<!DOCTYPE html>
<html lang="en">
<head>
<meta charset="utf-8">
<title>Gentle Willow Pregnancy and Baby Massage</title>
<link href="https://fonts.googleapis.com/css2?family=Playball&family=Arimo:ital,wght@0,400;0,700;1,400&display=swap" rel="stylesheet">
<style>
:root{
  --pink:#b96fa8;
  --pink-deep:#b0589e;
  --purple:#8b7cbc;
  --purple-btn:#8e7fbb;
  --grey-text:#6b6b6b;
  --line:#d4d4d4;
  --white:#ffffff;
  --script:'Playball', cursive;
  --sans:'Arimo', Arial, sans-serif;
}
*{margin:0;padding:0;box-sizing:border-box}
html,body{width:795px;height:1200px;overflow:hidden;background:var(--white)}
.page{position:relative;width:795px;height:1200px;font-family:var(--sans);overflow:hidden}
.abs{position:absolute}

/* hero */
.hero-photo{left:0;top:0;width:795px;height:449px;
  background:linear-gradient(100deg,#c9c1bb 0%,#bcb1a9 30%,#8d7f77 58%,#3d3734 78%,#2a2624 100%)}
.topbar{left:0;top:0;width:795px;height:68px;background:rgba(215,215,215,.82)}
.brand{left:50px;top:12px;width:84px;display:flex;flex-direction:column;align-items:center;gap:3px}
.brand-dot{width:16px;height:16px;border-radius:50%;background:var(--pink)}
.brand-name{font-family:var(--script);font-size:14px;color:var(--pink);line-height:1;white-space:nowrap}
.nav{left:149px;top:29px;display:flex;font-size:9.6px;color:var(--white);white-space:nowrap}
.nav span.sep{margin:0 6px}
.hero-title{left:0;width:795px;top:120px;text-align:center;font-family:var(--script);font-size:56px;color:var(--white);text-shadow:2px 3px 4px rgba(0,0,0,.45)}
.hero-quote{left:170px;width:455px;top:202px;text-align:center;font-style:italic;font-size:12.4px;line-height:17px;color:var(--white)}
.hero-btn{left:323px;top:253px;width:150px;height:40px;border:1px solid var(--white);border-radius:20px;color:var(--white);font-size:14px;display:flex;align-items:center;justify-content:center}

/* services */
.service-band{left:0;top:449px;width:795px;height:241px;background:var(--pink)}
.divider{top:449px;width:1px;height:241px;background:rgba(255,255,255,.75)}
.service{top:414px;width:166px}
.service-frame{width:166px;height:138px;background:var(--pink);padding:7px}
.service-photo{width:152px;height:124px}
.service-title{margin-top:7px;text-align:center;font-family:var(--script);font-size:20px;line-height:20px;color:var(--white);height:46px}
.service-text{margin-top:11px;padding:0 6px;text-align:center;font-size:9.5px;line-height:14px;color:var(--white)}
.pill{top:670px;width:110px;height:36px;border-radius:18px;background:var(--purple-btn);color:var(--white);font-size:14px;display:flex;align-items:center;justify-content:center;box-shadow:3px 3px 4px rgba(0,0,0,.35)}

/* welcome */
.col-divider{left:397px;top:690px;width:4px;height:345px;background:linear-gradient(90deg,#e4e4e4,#fff)}
.welcome-title{left:50px;top:735px;font-family:var(--script);font-size:32px;white-space:nowrap}
.welcome-title .a{color:var(--pink-deep)}
.welcome-title .b{color:var(--purple)}
.heart{left:52px;top:800px}
.welcome-text{font-size:9.8px;line-height:16.6px;color:var(--grey-text);white-space:nowrap}
.welcome-text.beside{left:188px;top:797px}
.welcome-text.below{left:52px;top:913px}
.learn-btn{left:52px;top:957px;width:138px;height:38px;background:var(--purple-btn);color:var(--white);font-size:14px;display:flex;align-items:center;justify-content:center}

/* testimonial */
.testi-title{left:425px;top:735px;display:flex;align-items:center;gap:6px;font-family:var(--script);font-size:32px;white-space:nowrap}
.testi-title .a{color:var(--pink-deep)}
.testi-title .b{color:var(--purple)}
.quote-box{left:426px;top:785px;width:304px;height:175px;border:1px solid var(--line);padding:11px 15px}
.quote-box p{font-size:9.5px;line-height:16.6px;color:var(--grey-text)}
.author{margin-top:6px;font-size:11px;color:var(--pink-deep)}
.author-role{font-size:9.5px;color:var(--purple)}
.client-photo{left:626px;top:915px;width:90px;height:90px;border-radius:50%;border:4px solid var(--pink);background:linear-gradient(160deg,#6a4a3a,#2a1e1a)}
.arrow{top:971px;width:24px;height:24px;display:flex;align-items:center;justify-content:center}

/* footer */
.rule{left:0;top:1035px;width:795px;height:5px;background:var(--pink)}
.footer{left:0;top:1048px;width:795px;height:152px;background:linear-gradient(90deg,#8c86c4,#b96fa6)}
.footer-line{left:0;top:1144px;width:795px;height:1px;background:rgba(255,255,255,.5)}
.f-item{top:1083px;display:flex;gap:8px;font-size:9.6px;line-height:14px;color:var(--white)}
.social{top:1078px;width:31px;height:31px;border-radius:50%;display:flex;align-items:center;justify-content:center;font-size:12px;font-weight:700}
.social.filled{background:var(--white);color:var(--pink)}
.social.ring{border:1.5px solid var(--white);color:var(--white)}
.copy{left:52px;top:1163px;display:flex;align-items:center;gap:5px;font-size:9.6px;color:var(--white)}
.copy .script{font-family:var(--script);font-size:13px}
.sitemap{left:695px;top:1165px;font-size:9.6px;color:var(--white);text-decoration:underline}
</style>
</head>
<body>
<div class="page">

  <div class="abs hero-photo" role="img" aria-label="Photo of a pregnant woman lying down receiving a gentle massage"></div>
  <header class="abs topbar"></header>
  <div class="abs brand"><span class="brand-dot"></span><span class="brand-name">Gentle Willow</span></div>
  <nav class="abs nav">
    <span>Home</span><span class="sep">|</span><span>About Me</span><span class="sep">|</span><span>Pregnancy Massage</span><span class="sep">|</span><span>Baby Massage</span><span class="sep">|</span><span>Pregnancy Massage Sessions</span><span class="sep">|</span><span>Baby Massage Sessions</span><span class="sep">|</span><span>Contact us</span>
  </nav>
  <h1 class="abs hero-title">Gentle Willow</h1>
  <p class="abs hero-quote">“Being touched and caressed,being massaged,is food for the infant.Food as necessary as minerals, vitamins, and proteins.”</p>
  <div class="abs hero-btn">CONTACT US</div>

  <section class="abs service-band"></section>
  <div class="abs divider" style="left:222px"></div>
  <div class="abs divider" style="left:398px"></div>
  <div class="abs divider" style="left:574px"></div>

  <div class="abs service" style="left:51px">
    <div class="service-frame"><div class="service-photo" role="img" aria-label="Photo of a pregnancy massage on a treatment table" style="background:linear-gradient(160deg,#f3f1ef,#d9cfc8 60%,#9cc3cf)"></div></div>
    <h2 class="service-title">Pregnancy Massage</h2>
    <p class="service-text">Lorem Ipsum is simply dummy text of the printing and typesetting industry. Lorem Ipsum has been</p>
  </div>
  <div class="abs service" style="left:227px">
    <div class="service-frame"><div class="service-photo" role="img" aria-label="Photo of hands massaging a baby's foot" style="background:linear-gradient(140deg,#f4e8e2,#f0cdb8 55%,#e7b49b)"></div></div>
    <h2 class="service-title">Baby Massage</h2>
    <p class="service-text">Lorem Ipsum is simply dummy text of the printing and typesetting industry. Lorem Ipsum has been</p>
  </div>
  <div class="abs service" style="left:403px">
    <div class="service-frame"><div class="service-photo" role="img" aria-label="Photo of a pregnant woman in a massage session" style="background:linear-gradient(120deg,#ebe5e0,#d8b9a4 55%,#2b2725)"></div></div>
    <h2 class="service-title">Pregnancy Massage Session</h2>
    <p class="service-text">Lorem Ipsum is simply dummy text of the printing and typesetting industry. Lorem Ipsum has been</p>
  </div>
  <div class="abs service" style="left:579px">
    <div class="service-frame"><div class="service-photo" role="img" aria-label="Photo of a baby lying on a blanket" style="background:linear-gradient(150deg,#f5f2ef,#ecd6c8 55%,#e8e4e0)"></div></div>
    <h2 class="service-title">Baby Massage Sessions</h2>
    <p class="service-text">Lorem Ipsum is simply dummy text of the printing and typesetting industry. Lorem Ipsum has been</p>
  </div>

  <div class="abs pill" style="left:79px">READ MORE</div>
  <div class="abs pill" style="left:252px">READ MORE</div>
  <div class="abs pill" style="left:432px">READ MORE</div>
  <div class="abs pill" style="left:605px">READ MORE</div>

  <div class="abs col-divider"></div>

  <h2 class="abs welcome-title"><span class="a">Welcome to </span><span class="b">Gentle Willow</span></h2>
  <svg class="abs heart" width="124" height="104" viewBox="0 0 128 108" role="img" aria-label="Heart-framed photo of two sleeping newborns">
    <path d="M64 106 C20 80 2 54 2 30 C2 10 18 0 34 0 C48 0 58 8 64 18 C70 8 80 0 94 0 C110 0 126 10 126 30 C126 54 108 80 64 106 Z" fill="#b96fa8"/>
    <path d="M64 92 C30 72 18 52 18 34 C18 20 28 13 39 13 C50 13 58 20 64 30 C70 20 78 13 89 13 C100 13 110 20 110 34 C110 52 98 72 64 92 Z" fill="#9c7a68"/>
  </svg>
  <div class="abs welcome-text beside">
    Gentle Willow Pregnancy and Baby Massage<br>
    was launched in 2017, offering massage for<br>
    pregnant women, and instruction of baby<br>
    massage to parents, grandparents and<br>
    carers.My vision is to provide a professional<br>
    massage service to pregnant mothers and<br>
    babies that also benefits from my skills.
  </div>
  <div class="abs welcome-text below">
    Lorem Ipsum is simply dummy text of the printing and typesetting industry<br>
    Lorem Ipsum is simply dummy text of the printing and typesetting industry
  </div>
  <div class="abs learn-btn">LEARN MORE</div>

  <h2 class="abs testi-title">
    <svg width="28" height="24" viewBox="0 0 28 24" aria-hidden="true"><path d="M0 24V13C0 5 4 1 11 0v4C7 5 5 8 5 11h6v13zM16 24V13c0-8 4-12 11-13v4c-4 1-6 4-6 7h6v13z" fill="#6e6e6e"/></svg>
    <span><span class="a">Client </span><span class="b">Testimonial</span></span>
  </h2>
  <div class="abs quote-box">
    <p>Lorem Ipsum is simply dummy text of the printing and typesetting industry. Lorem Ipsum has been the industry's standard dummy text ever since the 1500s, when an unknown printer took a galley of type and scrambled it to make a type specimen book. It has survived not only five centuries, but also the leap into electronic typesetting, remaining essentially unchanged.</p>
    <div class="author">- ABC ROSIE</div>
    <div class="author-role">Lorem Ipsum is simply dummy text</div>
  </div>
  <div class="abs client-photo" role="img" aria-label="Photo of a happy family with their baby"></div>
  <div class="abs arrow" style="left:426px;background:var(--pink)"><svg width="8" height="12" viewBox="0 0 8 12"><path d="M7 1 2 6l5 5" stroke="#fff" stroke-width="1.6" fill="none"/></svg></div>
  <div class="abs arrow" style="left:453px;background:var(--purple)"><svg width="8" height="12" viewBox="0 0 8 12"><path d="M1 1l5 5-5 5" stroke="#fff" stroke-width="1.6" fill="none"/></svg></div>

  <div class="abs rule"></div>
  <footer class="abs footer"></footer>
  <div class="abs f-item" style="left:50px">
    <svg width="11" height="14" viewBox="0 0 11 14"><path d="M5.5 0A5.5 5.5 0 0 0 0 5.5C0 9.5 5.5 14 5.5 14S11 9.5 11 5.5A5.5 5.5 0 0 0 5.5 0Zm0 7.6a2.1 2.1 0 1 1 0-4.2 2.1 2.1 0 0 1 0 4.2Z" fill="#fff"/></svg>
    <span>Maren Castell<br>Gentle Willow Pregnancy and<br>Infant Massage</span>
  </div>
  <div class="abs f-item" style="left:246px">
    <svg width="14" height="14" viewBox="0 0 14 14"><path d="M3 0 5 3.5 3.6 5.2c.9 2 2.5 3.6 4.6 4.6L9.9 8.4 13.5 10.4 12.7 13c-.3.7-1 1-1.7.9C5.6 13 1 8.4.1 3 0 2.3.3 1.6 1 1.3Z" fill="#fff"/></svg>
    <span>0412 555 019</span>
  </div>
  <div class="abs f-item" style="left:380px">
    <svg width="15" height="11" viewBox="0 0 15 11"><rect x=".6" y=".6" width="13.8" height="9.8" fill="none" stroke="#fff" stroke-width="1.2"/><path d="M.6.6 7.5 6 14.4.6" fill="none" stroke="#fff" stroke-width="1.2"/></svg>
    <span>maren.castell@gentle-willow.com.au</span>
  </div>
  <div class="abs social filled" style="left:630px" aria-label="Chatterlane">C</div>
  <div class="abs social ring" style="left:671px" aria-label="Flitter">F</div>
  <div class="abs social ring" style="left:712px" aria-label="Linkwise">L</div>
  <div class="abs footer-line"></div>
  <div class="abs copy"><span>©</span><span class="script">Gentle Willow</span><span>- 2017. All Rights Reserved</span></div>
  <div class="abs sitemap">Site Map</div>

</div>
</body>
</html>
```